Website homepage rework for women's travel website

I have a homepage (http://www.ladies-far-afield.com) that I'm 50% happy with but don't want to completely overhaul. I'd like to retain a similar look but upgrade it to something a bit more modern and less old-fashioned. The basic sense of the site is empowering, self-confident, fun and adventurous - but female and over 40.

A number of the elements on the page have to be redesigned, a few can be tweaked, and a few left alone. See the rest of the brief for further information.

Target Market(s)

women over 40 who like to travel

Industry/Entity Type

Travel

Number of Pages Required

1 page

Font styles to use
Other font styles liked:
• see my brief

Requirements
Must have
• - size - the page must be significantly wider
• - the only font I MUST keep is Raleway (as in the tagline) and possibly the font of the site name (Ladies Far Afield). Both of those work for me. There are too many fonts on the page, however, and that needs to be unified.
• - the rectangles I click to get inside the site have to change to something more modern, possibly square - they do not have to be separated into two columns as they are now, nor do they need the titles (toolkit etc)
• - I like the background image of the header - but it needs to be wider of course - also keep in mind the aspect - it has to fit into the smaller inside pages, whose size will not change
• - at the end of the project I need to receive the separate elements of the design so I can eventually make a change myself if needed ie. replace my own photo, for example
Nice to have
• - the three photos need to change to something more eye-popping - or something else should take their place to fill the space
Should not have
• I do not want a full, original redesign. I want my readers to still feel as though they are on the same site - same header, mostly same fonts.

```html
<!DOCTYPE html>
<html lang="en">
<head>
<meta charset="utf-8">
<title>Ladies Far Afield</title>
<link rel="stylesheet" href="https://fonts.googleapis.com/css2?family=Raleway:wght@400;600&family=Playfair+Display:ital@1&family=Oswald:wght@500&family=Roboto+Slab&family=Roboto&display=swap">
<style>
:root{
  --page:#000;
  --bar:#242424;
  --orange:#f7941d;
  --white:#fff;
  --ink:#333;
  --title-red:#f0400f;
  --search-bg:#f4f4f4;
  --search-btn:#d9250e;
}
*{margin:0;padding:0;box-sizing:border-box}
html,body{width:1200px;height:1180px;overflow:hidden;background:var(--page)}
body{position:relative;font-family:"Raleway",sans-serif}
.site{position:absolute;left:89px;top:0;width:1022px;height:1180px;background:var(--white)}
.nav{height:56px;background:var(--bar);display:flex;justify-content:center;align-items:center;gap:50px;padding-left:10px}
.nav a{color:var(--orange);text-decoration:none;font-size:15px;text-transform:uppercase;letter-spacing:.2px}
.header{position:relative;height:372px;overflow:hidden}
.header-bg{position:absolute;inset:0;background:radial-gradient(ellipse at 60% 20%,#ffd23a 0%,#f9a31c 40%,#e0620f 75%,#9a3a10 100%)}
.header-portrait{position:absolute;left:20px;top:56px;width:420px;height:316px;background:radial-gradient(ellipse at 45% 50%,#e9c6a6 0%,#c9b08a 40%,rgba(160,120,70,0) 75%)}
.header-road{position:absolute;left:300px;top:240px;width:600px;height:132px;background:linear-gradient(#b5602a,#6d5448)}
.brand{position:absolute;left:452px;top:61px}
.brand-name{display:inline-block;background:var(--title-red);color:var(--white);font-family:"Playfair Display",serif;font-style:italic;font-size:55px;line-height:62px;padding:0 20px 0 18px}
.tagline{font-size:27px;color:#2a2a2a;margin-top:4px;letter-spacing:.2px}
.snap{position:absolute;top:212px;width:138px;height:140px;background:var(--white);padding:8px 8px 28px;box-shadow:0 2px 6px rgba(0,0,0,.35)}
.snap span{display:block;width:100%;height:100%}
.snap-a{left:495px;transform:rotate(-4deg)}
.snap-a span{background:linear-gradient(#3aa0e0,#1e5f8a)}
.snap-b{left:640px;transform:rotate(2deg)}
.snap-b span{background:linear-gradient(#e58a5a,#2d8bc2)}
.snap-c{left:780px;transform:rotate(-3deg)}
.snap-c span{background:linear-gradient(#8bb84a,#c2453a)}
.intro{height:252px;text-align:center;padding-top:48px}
.intro h1{font-family:"Playfair Display",serif;font-style:italic;font-weight:400;color:var(--orange);font-size:37px;line-height:44px}
.intro p{font-size:16.5px;color:var(--ink);margin-top:2px}
.perks{list-style:none;text-align:left;width:580px;margin:14px 0 0 244px}
.perks li{font-size:17px;color:var(--ink);line-height:27px;display:flex;align-items:center;gap:10px}
.perks svg{flex:none}
.perks b{font-weight:600}
.cta{height:69px;background:var(--bar);text-align:center;font-family:"Playfair Display",serif;font-style:italic;color:var(--orange);font-size:36px;line-height:69px}
.cta a{color:var(--orange)}
.tiles{position:absolute;left:23px;top:791px;display:grid;grid-template-columns:repeat(3,323px);grid-auto-rows:93px;gap:5px 4px}
.tile{position:relative;overflow:hidden;background:#ccc}
.tile-band{height:60px;padding:7px 12px 0 14px;color:var(--white);overflow:hidden}
.tile-title{font-family:"Oswald",sans-serif;font-weight:500;font-size:24px;line-height:27px;text-transform:uppercase;letter-spacing:-.4px;white-space:nowrap}
.tile-sub{font-size:16.5px;line-height:21px;letter-spacing:-.1px;white-space:nowrap}
.tile-sub.slab{font-family:"Roboto Slab",serif;font-size:16.5px}
.tile-photo{height:33px}
.t-eating .tile-band{background:#f0501e}.t-eating .tile-photo{background:linear-gradient(90deg,#f3d8b8,#e98a3c,#f5e3cc)}
.t-packing .tile-band{background:#7c3d96}.t-packing .tile-photo{background:linear-gradient(90deg,#3b3560,#5a4f7a,#e0523a)}
.t-stress .tile-band{background:#0a9a1a}.t-stress .tile-photo{background:linear-gradient(90deg,#e0151b,#f24a1a,#c8101a)}
.t-argentina .tile-band{background:#f5d800}.t-argentina .tile-sub{color:#fff6b0}.t-argentina .tile-photo{background:linear-gradient(90deg,#3bb7c7,#c06a6a,#3bb7c7)}
.t-single .tile-band{background:#e0671c}.t-single .tile-photo{background:linear-gradient(90deg,#3a2a14,#d98a2a,#2c2010)}
.t-asia .tile-band{background:#d4141c}.t-asia .tile-photo{background:linear-gradient(90deg,#d8e6f2,#f0eadf,#d9e8c6)}
.t-carouge .tile-band{background:#33aef0}.t-carouge .tile-photo{background:linear-gradient(90deg,#b8b0a0,#e03040,#9a9488)}
.t-foodies .tile-band{background:#39d9c6}.t-foodies .tile-photo{background:linear-gradient(90deg,#f5f2ea,#f2b51e,#f5f2ea)}
.search{background:var(--search-bg);display:flex;align-items:center;padding-left:30px}
.search-field{width:250px;height:38px;background:var(--white);border:1px solid #ddd;border-right:0;font-family:"Roboto",sans-serif;font-size:11px;color:#666;line-height:36px;padding-left:10px}
.search-btn{width:40px;height:38px;background:var(--search-btn);display:flex;align-items:center;justify-content:center}
.footer{position:absolute;left:0;bottom:0;width:100%;height:56px;background:var(--bar);color:var(--white);font-family:"Roboto",sans-serif;font-size:14px;text-align:center;line-height:56px}
.share{position:absolute;left:0;top:388px;width:62px;text-align:center;color:var(--white);font-family:"Roboto",sans-serif}
.share-total{font-size:12px;font-weight:700;line-height:12px}
.share-total small{display:block;font-size:10px;font-weight:400}
.share-item{display:flex;flex-direction:column;align-items:center;margin-top:14px;font-size:9px;line-height:12px}
.share-dot{width:18px;height:18px;border-radius:50%;background:var(--white)}
</style>
</head>
<body>
<aside class="share">
  <div class="share-total">1.7k<small>Shares</small></div>
  <div class="share-item"><span class="share-dot"></span>1.5k</div>
  <div class="share-item"><span class="share-dot"></span>106</div>
  <div class="share-item"><span class="share-dot"></span></div>
  <div class="share-item"><span class="share-dot"></span></div>
  <div class="share-item"><svg width="22" height="16" viewBox="0 0 22 16"><rect x="1" y="1" width="20" height="14" fill="none" stroke="#fff" stroke-width="2"/><path d="M1 1l10 8 10-8" fill="none" stroke="#fff" stroke-width="2"/></svg></div>
  <div class="share-item"><span class="share-dot"></span></div>
</aside>

<div class="site">
  <nav class="nav">
    <a href="#">Start Here</a><a href="#">About</a><a href="#">Travel Resources</a><a href="#">Blog</a><a href="#">Travel Shop</a><a href="#">Contact</a>
  </nav>

  <header class="header">
    <div class="header-bg" role="img" aria-label="Warm orange old map blended with a desert road and red rock buttes"></div>
    <div class="header-road" role="img" aria-label="Desert road leading into the distance"></div>
    <div class="header-portrait" role="img" aria-label="Portrait of the site author smiling, sunglasses on her head"></div>
    <div class="brand">
      <div class="brand-name">Ladies Far Afield</div>
      <div class="tagline">For women who travel smart, safe + solo</div>
    </div>
    <div class="snap snap-a"><span role="img" aria-label="Palm trees by the sea"></span></div>
    <div class="snap snap-b"><span role="img" aria-label="Blue pots and agave against a terracotta wall"></span></div>
    <div class="snap snap-c"><span role="img" aria-label="Red scooter in a flowered street"></span></div>
  </header>

  <section class="intro">
    <h1>Hi, I’m Maren</h1>
    <p>I took my first solo trip at 15. I’ll show you how to travel...</p>
    <ul class="perks">
      <li><svg width="20" height="16" viewBox="0 0 20 16"><path d="M2 8l5 5L18 2" fill="none" stroke="#f7941d" stroke-width="3"/></svg><span><b>Smart</b>: practical tools to help you plan – and afford – the perfect trip</span></li>
      <li><svg width="20" height="16" viewBox="0 0 20 16"><path d="M2 8l5 5L18 2" fill="none" stroke="#f7941d" stroke-width="3"/></svg><span><b>Safe</b>: down-to-earth advice and a ton of safety recommendations</span></li>
      <li><svg width="20" height="16" viewBox="0 0 20 16"><path d="M2 8l5 5L18 2" fill="none" stroke="#f7941d" stroke-width="3"/></svg><span><b>Solo</b>: yes, you can do it!</span></li>
    </ul>
  </section>

  <div class="cta">Thinking of solo travel? <a href="#">Click here</a> to find out how.</div>

  <div class="tiles">
    <a class="tile t-eating"><div class="tile-band"><div class="tile-title">Eating with Locals</div><div class="tile-sub">The ultimate guide to social dining</div></div><div class="tile-photo" role="img" aria-label="Plated food"></div></a>
    <a class="tile t-packing"><div class="tile-band"><div class="tile-title">Your Packing List</div><div class="tile-sub slab">Take what you need - no more</div></div><div class="tile-photo" role="img" aria-label="Open suitcase with shoes"></div></a>
    <div class="tile search"><div class="search-field">Site Search</div><div class="search-btn"><svg width="14" height="14" viewBox="0 0 14 14"><circle cx="6" cy="6" r="4.2" fill="none" stroke="#fff" stroke-width="1.8"/><path d="M9 9l4 4" stroke="#fff" stroke-width="1.8"/></svg></div></div>
    <a class="tile t-stress"><div class="tile-band"><div class="tile-title">Stress Management Course</div><div class="tile-sub">How to travel stress-free</div></div><div class="tile-photo" role="img" aria-label="Red abstract graphic"></div></a>
    <a class="tile t-argentina"><div class="tile-band"><div class="tile-title">Solo in Argentina</div><div class="tile-sub">Does it really take two to tango?</div></div><div class="tile-photo" role="img" aria-label="Colourful harbour buildings"></div></a>
    <a class="tile t-single"><div class="tile-band"><div class="tile-title">No Single Supplement</div><div class="tile-sub slab">17 ways to avoid paying it</div></div><div class="tile-photo" role="img" aria-label="Sunset over a savanna"></div></a>
    <a class="tile t-asia"><div class="tile-band"><div class="tile-title">Solo Female Travel</div><div class="tile-sub">A 3-week Central Asia itinerary</div></div><div class="tile-photo" role="img" aria-label="Map of Central Asia with a route"></div></a>
    <a class="tile t-carouge"><div class="tile-band"><div class="tile-title">Rebellious Carouge</div><div class="tile-sub">Geneva’s Alter Ego?</div></div><div class="tile-photo" role="img" aria-label="Red café umbrellas on a square"></div></a>
    <a class="tile t-foodies"><div class="tile-band"><div class="tile-title">Europe for Foodies</div><div class="tile-sub">9 top destinations to try in October</div></div><div class="tile-photo" role="img" aria-label="Plate of saffron risotto"></div></a>
  </div>

  <footer class="footer">Copyright 2016 | All Right Reserved</footer>
</div>
</body>
</html>
```